Corporate Two Sided Business Card

Looking for a Corporate "edgy" Modern look and feel for a business card

We are looking at two options. Dark background with our logo on it, white background with our logo on it - The background is more - Charcoal / Graphite then black

Details will be

Danielle Forsk

Licensee / Director

m. 0428 519 064

e. danielle@quorvela.com.au

quorvela.com.au

Target Market(s)

Professional Business people that refer use business and clients that own Investment Properties

Industry/Entity Type

Business

Contact Information for Business Card

Details will be

Danielle Forsk

Licensee / Director

m. 0428 519 064

quorvela.com.au

Font styles to use
Serif

Colors
000000
ec1f27
eeeeee
ffffff

Requirements
Must have
• Two options - White Background and Dark Background. - Two sided
Nice to have
• A design that is edgy, modern and new to look instead of boring style corporate cards - It should be a full integrated design
Should not have
• Block looking - Cheap.

```html
<!DOCTYPE html>
<html lang="en">
<head>
<meta charset="utf-8">
<title>Quorvela – Business Card</title>
<link href="https://fonts.googleapis.com/css2?family=Kumbh+Sans:wght@500;600&family=Questrial&display=swap" rel="stylesheet">
<style>
  :root {
    --page-bg: #e5e5e5;
    --graphite-dark: #3a3b3d;
    --graphite-mid: #58595b;
    --graphite-light: #7d7d7d;
    --ink-white: #ffffff;
    --ink-soft: #e6e6e6;
    --accent-red: #ec1f27;
  }
  * { margin: 0; padding: 0; box-sizing: border-box; }
  html, body {
    width: 1200px; height: 568px; overflow: hidden;
    background: var(--page-bg);
  }
  .card {
    position: absolute; top: 157px;
    width: 422px; height: 254px;
    overflow: hidden;
    color: var(--ink-white);
  }
  .card--front {
    left: 161px;
    background: linear-gradient(200deg, var(--graphite-light) 0%, var(--graphite-mid) 40%, var(--graphite-dark) 100%);
  }
  .card--back {
    left: 617px;
    background: linear-gradient(160deg, var(--graphite-dark) 0%, var(--graphite-mid) 50%, var(--graphite-light) 100%);
  }
  .decor-area {
    position: absolute; top: 0; bottom: 0; width: 240px;
    background: radial-gradient(ellipse at 50% 40%, rgba(255,255,255,0.05), rgba(0,0,0,0.04) 70%, transparent 100%);
  }
  .card--front .decor-area { right: 0; }
  .card--back .decor-area { left: 0; }
  .contact-block { position: absolute; left: 23px; top: 30px; }
  .person-name {
    font-family: "Kumbh Sans", sans-serif; font-weight: 600;
    font-size: 17px; line-height: 20px; letter-spacing: 0.1px;
  }
  .person-role {
    font-family: "Questrial", sans-serif;
    font-size: 10px; line-height: 12px; color: var(--ink-soft);
  }
  .contact-list { list-style: none; margin-top: 19px; }
  .contact-item {
    display: flex; align-items: center; gap: 9px;
    font-family: "Questrial", sans-serif;
    font-size: 12px; line-height: 15.5px; color: var(--ink-soft);
  }
  .contact-icon { width: 9px; height: 9px; fill: var(--ink-white); flex: none; }
  .brand {
    position: absolute; bottom: 22px;
    display: flex; align-items: center; gap: 7px;
  }
  .card--front .brand { left: 23px; }
  .card--back .brand { right: 21px; }
  .brand-square { width: 14px; height: 14px; background: var(--accent-red); }
  .brand-name {
    font-family: "Kumbh Sans", sans-serif; font-weight: 500;
    font-size: 32px; line-height: 32px; letter-spacing: 0.3px;
    color: var(--ink-white);
  }
</style>
</head>
<body>
  <section class="card card--front">
    <div class="decor-area" role="img" aria-label="Large faint house silhouette decoration"></div>
    <div class="contact-block">
      <h1 class="person-name">Danielle Forsk</h1>
      <p class="person-role">Licensee / Director</p>
      <ul class="contact-list">
        <li class="contact-item">
          <svg class="contact-icon" viewBox="0 0 10 10"><path d="M2 0.5 L3.6 2.6 L2.7 3.6 C3.3 5 4.8 6.6 6.3 7.2 L7.3 6.3 L9.5 7.9 L8.4 9.4 C4.6 9.4 0.5 5.4 0.6 1.6 Z"/></svg>
          <span>0428 519 064</span>
        </li>
        <li class="contact-item">
          <svg class="contact-icon" viewBox="0 0 10 10"><path d="M0 2 H10 V8.5 H0 Z M0.6 2.5 L5 5.8 L9.4 2.5" stroke="#58595b" stroke-width="0.8"/></svg>
          <span>danielle@quorvela.com.au</span>
        </li>
        <li class="contact-item">
          <svg class="contact-icon" viewBox="0 0 10 10"><circle cx="5" cy="5" r="4.5"/><path d="M0.5 5 H9.5 M5 0.5 V9.5 M1.5 2.7 H8.5 M1.5 7.3 H8.5" stroke="#58595b" stroke-width="0.6" fill="none"/></svg>
          <span>www.quorvela.com.au</span>
        </li>
      </ul>
    </div>
    <div class="brand">
      <span class="brand-square"></span>
      <span class="brand-name">quorvela</span>
    </div>
  </section>

  <section class="card card--back">
    <div class="decor-area" role="img" aria-label="Large faint house silhouette decoration"></div>
    <div class="brand">
      <span class="brand-square"></span>
      <span class="brand-name">quorvela</span>
    </div>
  </section>
</body>
</html>
```